Evening on Willow Quay

I need a jpeg of a poster advertising a church party
It has a jazzy, fun theme. Details

An Evening on Willow Quay
Friday, June 14th from 8-11 PM
Party for all Ridgeline Parish adults at the Stake Centre
Fun, food, friends,live music, a chance to mingle and relax!
A great chance to bring your friends for a fun evening!

Id like some sort of jazz picture or shadowy picture....not really sure but I need it super fast so that I can have it printed Saturday...can anyone help me? I want it to be fun and snappy looking without being racy...no naked women :)

• naked or half dressed women, cigarettes, alcohol

```html
<!DOCTYPE html>
<html lang="en">
<head>
<meta charset="utf-8">
<title>An Evening on Willow Quay</title>
<link rel="stylesheet" href="https://fonts.googleapis.com/css2?family=Cinzel:wght@400;600&family=Marcellus+SC&display=swap">
<style>
  :root {
    --canvas-bg: #e9e7e4;
    --poster-edge: #f4f2ee;
    --night-top: #9a9a9a;
    --night-mid: #3b3b3b;
    --night-deep: #121212;
    --fire-hot: #ffd27a;
    --fire-mid: #f08a1e;
    --fire-dark: #5a1a04;
    --key-ivory: #f5e6c4;
    --key-shadow: #2a1608;
    --title-ink: #ffffff;
    --panel-veil: rgba(255, 255, 255, 0.42);
    --panel-ink: #3f3f3f;
  }
  * { box-sizing: border-box; margin: 0; padding: 0; }
  html, body {
    width: 1200px;
    height: 803px;
    overflow: hidden;
    background: var(--canvas-bg);
  }
  .poster {
    position: absolute;
    left: 330px;
    top: 22px;
    width: 540px;
    height: 758px;
    background: var(--night-deep);
    border: 6px solid var(--poster-edge);
    overflow: hidden;
    box-shadow: 0 6px 18px rgba(0, 0, 0, 0.25);
  }
  .city-photo {
    position: absolute;
    left: 0; top: 0;
    width: 100%;
    height: 440px;
    background:
      radial-gradient(ellipse 60% 18% at 62% 40%, rgba(255,255,255,0.75), rgba(255,255,255,0) 70%),
      linear-gradient(180deg, var(--night-top) 0%, var(--night-mid) 30%, #5e5e5e 42%, var(--night-mid) 60%, var(--night-deep) 100%);
  }
  .fire-illustration {
    position: absolute;
    left: 0;
    top: 330px;
    width: 100%;
    height: 300px;
    background:
      radial-gradient(ellipse 30% 45% at 18% 55%, rgba(255, 190, 90, 0.85), rgba(255, 190, 90, 0) 70%),
      radial-gradient(ellipse 30% 45% at 82% 55%, rgba(255, 190, 90, 0.85), rgba(255, 190, 90, 0) 70%),
      linear-gradient(180deg, rgba(18,18,18,0) 0%, var(--fire-dark) 25%, var(--fire-mid) 65%, var(--fire-hot) 100%);
  }
  .piano-keys {
    position: absolute;
    left: 0;
    bottom: 0;
    width: 100%;
    height: 150px;
    background: linear-gradient(180deg, var(--key-shadow) 0%, #c69a52 35%, var(--key-ivory) 70%, #d9c49a 100%);
  }
  .title {
    position: absolute;
    left: 0;
    top: 18px;
    width: 100%;
    text-align: center;
    font-family: "Cinzel", serif;
    font-weight: 400;
    color: var(--title-ink);
    font-size: 42px;
    line-height: 70px;
    letter-spacing: 0.5px;
    text-shadow: 0 2px 6px rgba(0, 0, 0, 0.6);
  }
  .details-panel {
    position: absolute;
    left: 108px;
    top: 202px;
    width: 306px;
    height: 366px;
    background: var(--panel-veil);
    text-align: center;
    font-family: "Marcellus SC", serif;
    color: var(--panel-ink);
  }
  .details-panel .day {
    margin-top: 30px;
    font-size: 28px;
    line-height: 32px;
  }
  .details-panel .date {
    font-size: 21px;
    line-height: 28px;
  }
  .details-panel .time {
    font-family: "Cinzel", serif;
    font-weight: 600;
    font-size: 44px;
    line-height: 58px;
  }
  .details-panel .blurb {
    margin-top: 26px;
    font-size: 16px;
    line-height: 25px;
  }
  .details-panel .blurb + .blurb { margin-top: 8px; }
</style>
</head>
<body>
  <main class="poster">
    <div class="city-photo" role="img" aria-label="Black and white photo of a city street at night with light trails between tall buildings"></div>
    <div class="fire-illustration" role="img" aria-label="Illustration of jazz trumpet and saxophone players outlined in gold amid rising flames"></div>
    <div class="piano-keys" role="img" aria-label="Illustration of glowing piano keys at the foot of the flames"></div>

    <h1 class="title">An Evening on<br>Willow Quay</h1>

    <section class="details-panel">
      <p class="day">Friday</p>
      <p class="date">June 14th from</p>
      <p class="time">8-11 PM</p>
      <p class="blurb">Party for all Ridgeline Parish<br>adults at the Stake Centre</p>
      <p class="blurb">Fun, food, friends, live music,<br>a chance to mingle and relax!</p>
      <p class="blurb">A great chance to bring<br>your friends for a fun evening!</p>
    </section>
  </main>
</body>
</html>
```